Simple Business Cards for Self-employed Coach

Simple business card with a design that includes the QLT logo.
Using either only the logo color or additional colors that match the logo.

Meridian Guides reach deeply into the past, gathering wisdom from East and West, while still staying current with the frontiers of new discovery in cognitive science, genetics, and other disciplines. see https://www.brightharborpath.example/what-is-integral-coaching/

Target Market(s)

Coaching Clients in Tokyo /Asia; in business organizations, but also outside

Industry/Entity Type

Life Coaching

Contact Information for Business Card

Lukas Brenning
Certified Meridian Guide

3-2-48 Kamiyoshi
Nakarino 164-0392
Tokyo, Japan

Phone: +81 70 4817 5062
E-Mail: lukas.brenning@mailora.example

Font styles to use
Sans Serif

Colors
00a990

Requirements
Must have
• include uploaded logo
• color fitting with QLT logo color
Nice to have
• simple, elegant design
Should not have
• clutter

```html
<!DOCTYPE html>
<html lang="en">
<head>
<meta charset="utf-8">
<title>Lukas Brenning – Business Card</title>
<link rel="stylesheet" href="https://fonts.googleapis.com/css2?family=Open+Sans:ital,wght@0,400;0,600;0,700;1,400&display=swap">
<style>
  :root {
    --teal: #00a990;
    --teal-dark: #008a76;
    --teal-light: #1fb9a1;
    --white: #ffffff;
    --paper: #fbfbfb;
    --ground: #eceff0;
    --ink: #1f2a2a;
  }
  * { box-sizing: border-box; margin: 0; padding: 0; }
  html, body {
    width: 865px; height: 1200px; overflow: hidden;
    background: var(--ground);
    font-family: "Open Sans", Arial, sans-serif;
  }
  .sheet {
    position: relative; width: 865px; height: 1200px;
  }
  .card {
    position: absolute; left: 32px; width: 800px; height: 470px;
    background: var(--paper);
    box-shadow: 0 6px 22px rgba(0,0,0,.16);
    overflow: hidden;
  }
  .card--front { top: 90px; }
  .card--back { top: 640px; }
  .card__shapes { position: absolute; inset: 0; width: 100%; height: 100%; }

  .brand {
    position: absolute; display: flex; align-items: center; gap: 14px;
    color: var(--teal); font-weight: 700; letter-spacing: 6px;
  }
  .brand__mark { width: 30px; height: 30px; background: var(--teal); }
  .card--front .brand { top: 46px; right: 56px; font-size: 46px; }
  .card--back .brand { top: 190px; left: 50%; transform: translateX(-50%); font-size: 64px; }
  .card--back .brand__mark { width: 42px; height: 42px; }

  .holder { position: absolute; left: 44px; top: 200px; color: var(--white); }
  .holder__name { font-size: 34px; font-weight: 400; line-height: 1.1; }
  .holder__title { font-size: 18px; font-style: italic; margin-top: 6px; }

  .contacts {
    position: absolute; left: 44px; top: 290px; list-style: none;
    color: var(--white); font-size: 21px; line-height: 1.3;
  }
  .contacts__item { display: flex; align-items: flex-start; gap: 16px; margin-bottom: 12px; }
  .contacts__icon {
    flex: none; width: 34px; height: 34px; border-radius: 50%;
    background: var(--white); display: flex; align-items: center; justify-content: center;
  }
  .contacts__icon svg { width: 18px; height: 18px; fill: var(--teal); }
  .contacts__text { padding-top: 2px; }
</style>
</head>
<body>
<main class="sheet">

  <section class="card card--front" aria-label="Business card front">
    <svg class="card__shapes" viewBox="0 0 800 470" preserveAspectRatio="none" aria-hidden="true">
      <polygon points="0,0 270,0 620,470 0,470" fill="var(--teal)"/>
      <polygon points="270,0 300,0 650,470 620,470" fill="var(--teal-light)" opacity=".55"/>
      <polygon points="0,0 270,0 140,0 0,190" fill="var(--teal-dark)" opacity=".35"/>
    </svg>

    <div class="brand"><span class="brand__mark"></span>QLT</div>

    <div class="holder">
      <h1 class="holder__name">Lukas Brenning</h1>
      <p class="holder__title">Certified Meridian Guide</p>
    </div>

    <ul class="contacts">
      <li class="contacts__item">
        <span class="contacts__icon"><svg viewBox="0 0 24 24"><path d="M6.6 10.8a15.1 15.1 0 0 0 6.6 6.6l2.2-2.2c.3-.3.7-.4 1-.2 1.1.4 2.3.6 3.6.6.6 0 1 .4 1 1V20c0 .6-.4 1-1 1A17 17 0 0 1 3 4c0-.6.4-1 1-1h3.5c.6 0 1 .4 1 1 0 1.3.2 2.5.6 3.6.1.3 0 .7-.2 1z"/></svg></span>
        <span class="contacts__text">+81 70 4817 5062</span>
      </li>
      <li class="contacts__item">
        <span class="contacts__icon"><svg viewBox="0 0 24 24"><path d="M12 2a7 7 0 0 0-7 7c0 5.2 7 13 7 13s7-7.8 7-13a7 7 0 0 0-7-7zm0 9.5A2.5 2.5 0 1 1 12 6.5a2.5 2.5 0 0 1 0 5z"/></svg></span>
        <span class="contacts__text">3-2-48 Kamiyoshi<br>Nakarino 164-0392<br>Tokyo, Japan</span>
      </li>
      <li class="contacts__item">
        <span class="contacts__icon"><svg viewBox="0 0 24 24"><path d="M3 5h18v14H3z" opacity="0"/><path d="M4 5h16a1 1 0 0 1 1 1v12a1 1 0 0 1-1 1H4a1 1 0 0 1-1-1V6a1 1 0 0 1 1-1zm8 7 8-5H4z"/></svg></span>
        <span class="contacts__text">lukas.brenning@mailora.example</span>
      </li>
    </ul>
  </section>

  <section class="card card--back" aria-label="Business card back">
    <svg class="card__shapes" viewBox="0 0 800 470" preserveAspectRatio="none" aria-hidden="true">
      <polygon points="0,300 0,470 230,470" fill="var(--teal)"/>
      <polygon points="0,270 0,300 230,470 265,470" fill="var(--teal-light)" opacity=".55"/>
    </svg>
    <div class="brand"><span class="brand__mark"></span>QLT</div>
  </section>

</main>
</body>
</html>
```